Newspaper Ad

Please create an ad for a newspaper that is 10.5 wide and 13 inches long. Please highlight the features of the property and ensure that the name of our firm (Birchwood Hollow Realty) is the same size as our phone number which is 717-530-6198.

Pemberton's Crossing and The residences at 9 N. Ash
9 N. Ash Street, Quarryville PA

Now leasing 1, 2 & 3 bedroom units available this spring. Newley renovated apartments with stainless appliances, hardwood floors, granite countertops, in unit laundry. Includes water, sewer trash and off street parking. 1200sq first floor retail available.

717.530.6198 or www.BirchwoodHollowRealty.example for details.

```html
<!DOCTYPE html>
<html lang="en">
<head>
<meta charset="utf-8">
<title>Now Leasing – Birchwood Hollow Realty</title>
<link rel="stylesheet" href="https://fonts.googleapis.com/css2?family=Montserrat:wght@300;400;600;700;800&family=Open+Sans:ital,wght@1,600&display=swap">
<style>
:root{
  --backdrop:#8e8f91;
  --paper:#ffffff;
  --teal:#0e6c70;
  --silver:#c2c3c5;
  --ink:#333334;
  --slate:#58595b;
  --rule:#9a9a9a;
  --accent:#f4a63a;
  --phone:#e8e8e8;
}
*{margin:0;padding:0;box-sizing:border-box}
html,body{width:998px;height:1200px;overflow:hidden;background:var(--backdrop)}
body{font-family:"Montserrat",sans-serif;color:var(--ink);position:relative}
.ad{position:absolute;left:80px;top:79px;width:837px;height:1037px;background:var(--paper);overflow:hidden}
.hero-photo{position:absolute;left:0;top:0;width:837px;height:540px;
  background:linear-gradient(180deg,#c9d6e4 0%,#e4e9ef 22%,#9a9ea3 45%,#7d8186 70%,#45474c 100%);
  clip-path:polygon(0 0,837px 0,837px 478px,679px 536px,341px 374px,0 374px)}
.headline-box{position:absolute;left:0;top:167px;width:341px;height:207px;background:var(--teal)}
.headline-now{position:absolute;left:55px;top:28px;font-weight:800;font-size:93px;line-height:1;color:#fff;letter-spacing:-2px}
.headline-leasing{position:absolute;left:57px;top:119px;font-weight:800;font-size:52px;line-height:1;color:var(--silver);letter-spacing:-1px}
.units-count{position:absolute;left:55px;top:404px;font-weight:800;font-size:64px;line-height:1;color:var(--teal);letter-spacing:-1px}
.units-label{position:absolute;left:56px;top:467px;font-weight:800;font-size:43px;line-height:1;color:var(--teal);letter-spacing:-.5px}
.units-when{position:absolute;left:57px;top:513px;font-weight:800;font-size:32px;line-height:1;color:var(--slate);letter-spacing:-.3px}
.rule{position:absolute;left:57px;width:410px;height:1px;background:var(--rule)}
.location-pin{position:absolute;left:44px;top:575px;width:34px;height:48px}
.location-name{position:absolute;left:86px;top:584px;font-size:14.5px;font-weight:400;white-space:nowrap;color:var(--ink)}
.location-name b{font-weight:700}
.location-street{position:absolute;left:117px;top:606px;font-size:14.5px;font-weight:400;white-space:nowrap}
.features{position:absolute;left:57px;top:672px;width:410px;height:57px;display:flex;justify-content:space-between;list-style:none}
.feature{display:flex;flex-direction:column;align-items:center;padding-top:8px}
.feature svg{width:18px;height:18px;stroke:var(--slate);fill:none;stroke-width:1.4}
.feature span{font-family:"Open Sans",sans-serif;font-style:italic;font-weight:600;font-size:9.5px;line-height:9.5px;text-align:center;margin-top:3px;color:var(--slate)}
.description{position:absolute;left:57px;top:762px;width:420px;font-size:13.4px;font-weight:400;line-height:21px;color:var(--ink);letter-spacing:.2px}
.interior-photo{position:absolute;left:499px;width:311px;height:133px}
.living-room{top:564px;background:linear-gradient(135deg,#b99a7b 0%,#7b5a43 45%,#c7b9a9 100%)}
.kitchen{top:711px;background:linear-gradient(180deg,#e4e2df 0%,#8b8884 55%,#8a5a36 100%)}
.contact-band{position:absolute;left:0;top:877px;width:474px;height:160px;background:var(--teal);color:#fff;text-align:center}
.call-line{position:absolute;left:0;width:474px;top:16px;display:flex;justify-content:center;align-items:baseline;gap:12px;white-space:nowrap}
.call-label{color:var(--accent);font-size:18px;font-weight:600}
.call-phone{color:var(--phone);font-size:30px;font-weight:800;letter-spacing:-.3px;line-height:1.2}
.firm-name{position:absolute;left:0;width:474px;top:60px;font-size:30px;font-weight:800;line-height:1.2;letter-spacing:-.3px;white-space:nowrap}
.firm-address{position:absolute;left:0;width:474px;top:107px;font-size:12px;font-weight:600;letter-spacing:1.2px}
.firm-web{position:absolute;left:0;width:474px;top:129px;font-size:12px;font-weight:600;letter-spacing:1px}
.brand-mark{position:absolute;left:499px;top:873px;width:311px;height:130px;display:flex;align-items:center;justify-content:center;gap:10px}
.brand-square{width:14px;height:14px;background:var(--teal)}
.brand-name{font-size:22px;font-weight:600;color:var(--ink);white-space:nowrap}
</style>
</head>
<body>
<main class="ad">
  <div class="hero-photo" role="img" aria-label="Rendering of the renovated two-storey clapboard building with a wraparound porch and turret under a cloudy sky"></div>

  <div class="headline-box">
    <div class="headline-now">NOW</div>
    <div class="headline-leasing">LEASING</div>
  </div>

  <div class="units-count">1, 2 &amp; 3</div>
  <div class="units-label">BEDROOM UNITS</div>
  <div class="units-when">AVAILABLE THIS SPRING</div>

  <div class="rule" style="top:564px"></div>

  <svg class="location-pin" viewBox="0 0 34 48" aria-hidden="true">
    <path d="M17 2C9 2 3 8 3 16c0 10 14 29 14 29s14-19 14-29C31 8 25 2 17 2z" fill="none" stroke="#0e6c70" stroke-width="4"/>
    <circle cx="17" cy="16" r="5" fill="none" stroke="#0e6c70" stroke-width="3.5"/>
  </svg>
  <div class="location-name"><b>Pemberton's Crossing</b> and <b>The Residences</b></div>
  <div class="location-street">at 9 N. Ash Street, Quarryville PA</div>

  <div class="rule" style="top:671px"></div>
  <ul class="features">
    <li class="feature"><svg viewBox="0 0 18 18"><path d="M2 6V2h4M12 2h4v4M16 12v4h-4M6 16H2v-4"/><rect x="6.5" y="6.5" width="5" height="5"/></svg><span>1200<br>Sqm</span></li>
    <li class="feature"><svg viewBox="0 0 18 18"><path d="M2 4v11M2 12h14v3M2 9h14v3M4 9V7h4v2"/></svg><span>1-3<br>Bedrooms</span></li>
    <li class="feature"><svg viewBox="0 0 18 18"><rect x="4" y="1" width="10" height="16"/><path d="M4 7h10M6 3v2M6 9v3"/></svg><span>Stainless<br>Appliances</span></li>
    <li class="feature"><svg viewBox="0 0 18 18"><rect x="2" y="2" width="14" height="14"/><path d="M2 8l6-6M2 13L13 2M5 16L16 5M10 16l6-6"/></svg><span>Hardwood<br>Floors</span></li>
    <li class="feature"><svg viewBox="0 0 18 18"><rect x="1" y="4" width="16" height="11"/><rect x="3" y="7" width="5" height="5"/><rect x="10" y="7" width="5" height="5"/></svg><span>Granite<br>Countertops</span></li>
    <li class="feature"><svg viewBox="0 0 18 18"><rect x="3" y="1" width="12" height="16"/><circle cx="9" cy="10" r="4"/><circle cx="9" cy="10" r="2"/></svg><span>In Unit<br>Laundry</span></li>
  </ul>
  <div class="rule" style="top:729px"></div>

  <p class="description">Newley renovated apartments with stainless appliances, hardwood floors, granite countertops, in unit laundry. Includes water, sewer, trash and off street parking.1200 sq first floor retail available.</p>

  <div class="interior-photo living-room" role="img" aria-label="Living room with brick fireplace, sectional sofa and hardwood floor"></div>
  <div class="interior-photo kitchen" role="img" aria-label="Open kitchen with grey cabinets, stainless appliances and hardwood floor"></div>

  <section class="contact-band">
    <div class="call-line"><span class="call-label">Call Us Now!</span><span class="call-phone">717.530.6198</span></div>
    <div class="firm-name">Birchwood Hollow Realty</div>
    <div class="firm-address">2240 Meadowbrook Pike Quarryville, PA 17566</div>
    <div class="firm-web">www.BirchwoodHollowRealty.example</div>
  </section>

  <div class="brand-mark">
    <span class="brand-square"></span>
    <span class="brand-name">Birchwood Hollow Realty</span>
  </div>
</main>
</body>
</html>
```